Design for Certificate

Design a certificate for training, providing our company logo such as attachments. Company's name is "BRYNE Fjellvik Advisory Ltd", please refer to our company profile: https://www.bryne-fjellvik.example/company_info

The style of the current certificate is also attached, and another certificate of another company can be referred to. Psd & jpg are required for the final draft (the layers of psd are not merged). Thanks!

```html
<!DOCTYPE html>
<html lang="en">
<head>
<meta charset="utf-8">
<title>Certificate of Completion – BRYNE Fjellvik Advisory Ltd</title>
<link rel="stylesheet" href="https://fonts.googleapis.com/css2?family=Tinos:wght@400;700&display=swap">
<style>
  :root {
    --backdrop: #e9e6e5;
    --frame: #48494b;
    --paper: #f7f6f4;
    --ink: #1a1a1a;
    --rule: #2b2b2b;
    --brand-tan: #dcb49c;
    --watermark: #e4e2df;
    --watermark-line: #d9d6d2;
    --signature: #3a3d3a;
  }
  * { box-sizing: border-box; margin: 0; padding: 0; }
  html, body {
    width: 1200px; height: 1000px; overflow: hidden;
    background: var(--backdrop);
    font-family: "Tinos", "Times New Roman", serif;
    color: var(--ink);
  }
  .canvas { position: relative; width: 1200px; height: 1000px; }
  .certificate-frame {
    position: absolute; left: 250px; top: 12px; width: 690px; height: 973px;
    background: var(--frame);
  }
  .certificate-paper {
    position: absolute; left: 15px; top: 18px; width: 660px; height: 938px;
    background: var(--paper);
  }
  .brand-block {
    position: absolute; left: 232px; top: 43px; width: 199px; height: 164px;
    background: var(--frame);
    display: flex; align-items: center; justify-content: center; gap: 10px;
  }
  .brand-mark { width: 10px; height: 10px; background: var(--brand-tan); }
  .brand-name {
    color: var(--brand-tan); font-size: 40px; font-weight: 400; letter-spacing: 3px;
  }
  .title {
    position: absolute; left: 0; right: 0; top: 258px; text-align: center;
    font-size: 32px; font-weight: 400;
  }
  .awarded-to {
    position: absolute; left: 0; right: 0; top: 315px; text-align: center; font-size: 15px;
  }
  .recipient-line {
    position: absolute; left: 54px; width: 554px; top: 402px; border-top: 1px solid var(--rule);
  }
  .completed {
    position: absolute; left: 0; right: 0; top: 429px; text-align: center; font-size: 15px;
  }
  .course {
    position: absolute; left: 0; right: 0; top: 466px; text-align: center; font-size: 15px;
  }
  .course-name { font-weight: 700; font-size: 17px; }
  .duration {
    position: absolute; left: 162px; top: 507px; font-size: 15px;
    display: flex; align-items: flex-end; gap: 12px;
  }
  .blank { display: inline-block; border-bottom: 1px solid var(--rule); height: 12px; }
  .date-blank { width: 174px; }
  .emblem-panel {
    position: absolute; left: 233px; top: 550px; width: 198px; height: 326px;
  }
  .issuer {
    position: absolute; left: 420px; top: 614px; width: 160px; text-align: center;
    font-size: 17px; font-weight: 700; line-height: 23px;
  }
  .signature {
    position: absolute; left: 403px; top: 670px; width: 170px; height: 40px;
    background: linear-gradient(90deg, transparent, rgba(58,61,58,0.22) 20%, rgba(58,61,58,0.22) 80%, transparent);
    border-radius: 20px;
  }
  .signature-line {
    position: absolute; left: 388px; width: 220px; top: 712px; border-top: 1px solid var(--rule);
  }
  .signatory-role {
    position: absolute; left: 388px; width: 220px; top: 716px; text-align: center; font-size: 13px;
  }
  .certificate-number {
    position: absolute; left: 54px; top: 899px; font-size: 13px;
    display: flex; align-items: flex-end; gap: 10px;
  }
  .number-blank { width: 174px; height: 9px; }
</style>
</head>
<body>
<main class="canvas">
  <section class="certificate-frame">
    <div class="certificate-paper">
      <div class="brand-block">
        <span class="brand-mark"></span>
        <span class="brand-name">BRYNE</span>
      </div>

      <h1 class="title">Certificate of Completion</h1>
      <p class="awarded-to">This certificate is awarded to</p>
      <div class="recipient-line"></div>
      <p class="completed">has successfully completed</p>
      <p class="course"><span class="course-name">Brand Reputation Management</span> Training Course</p>
      <p class="duration">Sixteen hours,&nbsp; held on <span class="blank date-blank"></span></p>

      <svg class="emblem-panel" viewBox="0 0 198 326" role="img" aria-label="Faint framed brand emblem decoration">
        <rect x="1" y="1" width="186" height="316" fill="var(--watermark)" opacity="0.45" stroke="var(--watermark-line)" stroke-width="2"/>
        <rect x="11" y="16" width="186" height="309" fill="none" stroke="var(--watermark-line)" stroke-width="2"/>
      </svg>

      <p class="issuer">BRYNE Fjellvik Advisory Ltd</p>
      <div class="signature" role="img" aria-label="Handwritten signature of the Chief Technology Officer"></div>
      <div class="signature-line"></div>
      <p class="signatory-role">Chief Technology Officer</p>

      <p class="certificate-number">Certificate No.: <span class="blank number-blank"></span></p>
    </div>
  </section>
</main>
</body>
</html>
```